Letterhead and email signature block for school

We are a Remote School in the North West of Western Australia and I want to take our logo and use that to create a professional letter head and email signature block. A sample signature block is attached. For the Letterhead; The logo is also attached. I like the Orange and black combination of the logo, needs to include motto plus the following contact details;
PMB 3 BROOME WA
Phone: (08) 9176 3058
Fax: (08) 9176 3047
ABN: 41 297 580 114

The email signature block needs to have the following;
Devon Lukas Farrow
Principal
Tallowood Creek RCS
Phone: (08) 9176 3058
Fax: (08) 9176 3047
Mobile: 0455 318 207
Email: Devon.Farrow@learnwave.edu.au

Target Market(s)

Parents

Industry/Entity Type

Education

Contact Information for Business Card

Devon Lukas Farrow
Principal
Tallowood Creek RCS
Phone: (08) 9176 3058
Fax: (08) 9176 3047
Mobile: 0455 318 207

Colors
f37122
000000

Requirements
Must have
• see breif

```html
<!DOCTYPE html>
<html lang="en">
<head>
<meta charset="utf-8">
<title>Tallowood Creek RCS Letterhead</title>
<link href="https://fonts.googleapis.com/css2?family=Oswald:wght@300;400;500&display=swap" rel="stylesheet">
<style>
  :root {
    --orange: #f37122;
    --black: #000000;
    --ink: #4a4a4a;
    --grey-bar: #a9a9ab;
    --stage: #f6ddbb;
    --paper: #ffffff;
    --swoosh-grey: #ececec;
    --swoosh-peach: #fdf1e6;
  }
  html, body {
    margin: 0;
    width: 1200px;
    height: 784px;
    overflow: hidden;
    background: var(--stage);
    font-family: "Oswald", sans-serif;
  }
  .letterhead {
    position: absolute;
    left: 338px;
    top: 22px;
    width: 523px;
    height: 740px;
    background: var(--paper);
    box-shadow: 0 6px 18px rgba(120, 80, 30, 0.18);
    overflow: hidden;
  }
  .top-rule {
    position: absolute;
    top: 20px;
    height: 4px;
  }
  .top-rule--grey {
    left: 0;
    width: 160px;
    background: linear-gradient(90deg, #d6d6d8, var(--grey-bar));
  }
  .top-rule--orange {
    left: 300px;
    right: 0;
    top: 112px;
    background: var(--orange);
  }
  .brand {
    position: absolute;
    left: 172px;
    top: 36px;
    width: 120px;
    text-align: center;
  }
  .brand__mark {
    width: 46px;
    height: 46px;
    margin: 0 auto 6px;
    border-radius: 50%;
    background: var(--orange);
  }
  .brand__name {
    font-weight: 500;
    font-size: 15px;
    line-height: 1.1;
    color: var(--black);
  }
  .brand__motto {
    font-weight: 300;
    font-size: 8px;
    color: var(--black);
    margin-top: 2px;
  }
  .swoosh {
    position: absolute;
    left: 0;
    bottom: 0;
    width: 523px;
    height: 330px;
  }
  .contact {
    position: absolute;
    left: 14px;
    bottom: 24px;
    display: flex;
    gap: 18px;
    font-weight: 300;
    font-size: 11px;
    color: var(--ink);
  }
  .contact__item {
    display: flex;
    align-items: center;
    gap: 5px;
  }
  .contact__icon {
    width: 10px;
    height: 10px;
  }
  .base-band {
    position: absolute;
    bottom: 0;
    height: 9px;
  }
  .base-band--orange {
    left: 0;
    width: 384px;
    background: var(--orange);
  }
  .base-band--dark {
    left: 392px;
    right: 0;
    background: linear-gradient(90deg, #9a9a9a, #111);
  }
</style>
</head>
<body>
  <main class="letterhead">
    <div class="top-rule top-rule--grey"></div>
    <div class="brand">
      <div class="brand__mark"></div>
      <div class="brand__name">Tallowood Creek RCS</div>
      <div class="brand__motto">Learning together for our future</div>
    </div>
    <div class="top-rule top-rule--orange"></div>

    <svg class="swoosh" viewBox="0 0 523 330" aria-hidden="true">
      <path d="M0 330 L0 0 C60 10 80 90 150 160 C230 240 330 270 420 330 Z" fill="var(--swoosh-peach)"/>
      <path d="M60 0 C110 60 150 120 240 170 C300 205 340 215 380 230 C320 215 260 195 210 170 C140 130 100 70 60 0 Z" fill="var(--swoosh-grey)"/>
      <path d="M0 160 C120 170 220 220 340 300 C250 245 140 195 0 185 Z" fill="#fbe6d4"/>
    </svg>

    <div class="contact">
      <span class="contact__item">
        <svg class="contact__icon" viewBox="0 0 10 10"><circle cx="5" cy="5" r="5" fill="var(--orange)"/><circle cx="5" cy="4.2" r="1.6" fill="#fff"/></svg>
        PMB 3 BROOME WA
      </span>
      <span class="contact__item">
        <svg class="contact__icon" viewBox="0 0 10 10"><circle cx="5" cy="5" r="5" fill="var(--orange)"/><rect x="3.5" y="2.5" width="3" height="5" rx="0.6" fill="#fff"/></svg>
        (08) 9176 3058
      </span>
      <span class="contact__item">
        <svg class="contact__icon" viewBox="0 0 10 10"><circle cx="5" cy="5" r="5" fill="var(--orange)"/><rect x="2.8" y="3.2" width="4.4" height="3.6" fill="#fff"/></svg>
        (08) 9176 3047
      </span>
      <span class="contact__item">
        <svg class="contact__icon" viewBox="0 0 10 10"><circle cx="5" cy="5" r="5" fill="var(--orange)"/><circle cx="5" cy="5" r="1.8" fill="#fff"/></svg>
        ABN: 41 297 580 114
      </span>
    </div>

    <div class="base-band base-band--orange"></div>
    <div class="base-band base-band--dark"></div>
  </main>
</body>
</html>
```